Stationery and Business Cards
PulseHaven
Bright & Fun-filled
Tessa Lund
Massage Therapist
42 Caxbury Vale Road
London
e4 8QT
massage@pulsehaven.co.uk
www.pulsehaven.co.uk

```html
<!DOCTYPE html>
<html lang="en">
<head>
<meta charset="utf-8">
<title>PulseHaven Business Cards</title>
<link rel="stylesheet" href="https://fonts.googleapis.com/css2?family=Montserrat:wght@800&family=Arimo:wght@400;700&display=swap">
<style>
  :root {
    --navy: #1c3a56;
    --mint: #86c6ad;
    --mint-light: #c9e6da;
    --card: #ffffff;
    --ink: #2a2f36;
    --backdrop: #e7e8ea;
  }
  * { margin: 0; padding: 0; box-sizing: border-box; }
  html, body {
    width: 1200px; height: 1002px; overflow: hidden;
    background: var(--backdrop);
  }
  .sheet { position: relative; width: 1200px; height: 1002px; }
  .card {
    position: absolute; left: 220px;
    width: 760px; height: 434px;
    background: var(--card);
    border-radius: 14px;
    box-shadow: 0 4px 18px rgba(0,0,0,0.12);
    overflow: hidden;
  }
  .card--front { top: 52px; }
  .card--back { top: 516px; }

  .brand__name {
    font-family: "Montserrat", sans-serif; font-weight: 800;
    color: var(--navy); line-height: 1; letter-spacing: -0.5px;
  }

  .card--front .brand { position: absolute; left: 44px; top: 70px; }
  .card--front .brand__name { font-size: 54px; }

  .holder { position: absolute; left: 48px; top: 170px; font-family: "Arimo", sans-serif; }
  .holder__name { font-size: 24px; font-weight: 700; color: var(--navy); }
  .holder__role { font-size: 15px; color: var(--ink); margin-top: 4px; }

  .contact {
    position: absolute; left: 456px; top: 112px;
    font-family: "Arimo", sans-serif; font-size: 14px; line-height: 1.45; color: var(--ink);
  }
  .contact__block + .contact__block { margin-top: 16px; }

  .swoosh { position: absolute; left: 0; bottom: 0; width: 760px; height: 434px; }
  .web {
    position: absolute; right: 40px; bottom: 92px;
    font-family: "Arimo", sans-serif; font-size: 15px; color: #fff;
    transform: rotate(-12deg); transform-origin: right bottom;
  }

  .card--back .brand {
    position: absolute; left: 0; right: 0; top: 170px; text-align: center;
  }
  .card--back .brand__name { font-size: 82px; }
</style>
</head>
<body>
<main class="sheet">
  <section class="card card--front">
    <div class="brand">
      <div class="brand__name">PulseHaven</div>
    </div>
    <div class="holder">
      <div class="holder__name">Tessa Lund</div>
      <div class="holder__role">Massage Therapist</div>
    </div>
    <div class="contact">
      <div class="contact__block">42 Caxbury Vale Road<br>London<br>e4 8QT</div>
      <div class="contact__block">C: 07700 900417<br>E: massage@pulsehaven.co.uk</div>
    </div>
    <svg class="swoosh" viewBox="0 0 760 434" aria-hidden="true">
      <path d="M0,332 C210,382 470,330 760,210 L760,236 C470,352 210,400 0,352 Z" fill="var(--mint-light)"/>
      <path d="M0,346 C210,394 470,344 760,226 L760,232 C470,352 210,400 0,352 Z" fill="var(--mint)"/>
      <path d="M0,380 C220,418 480,370 760,256 L760,434 L0,434 Z" fill="var(--navy)"/>
    </svg>
    <div class="web">www.pulsehaven.co.uk</div>
  </section>

  <section class="card card--back">
    <div class="brand">
      <div class="brand__name">PulseHaven</div>
    </div>
  </section>
</main>
</body>
</html>
```